Local business providing residential house cleaning services

We need a business card design that is "cute" or "cartoonish" while still maintaining a professional appeal. Tidy Nook Cleaners is the name. We would like to use a "pin up girl" or maid next to the name with a broom or vacuum cleaner. We want the look to have a 50's American look to it. We are not sure if we want the pin up girl in a maid outfit or with a broom or vacuum cleaner but we hope some of you will be able to take these ideas and be creative. If you have any questions at all please don't hesitate to message me so that we can get the best design possible. Thank you very much and I look forward to seeing some designs! Mira Delgado

Target Market(s)

Upper class Americans that are busy and have money and want to come home to a clean house.

Industry/Entity Type

Cleaning Service

Contact Information for Business Card

Pin up girl incorporated into the card is a must.

Font styles to use
Decorative
Script

Requirements
Must have
• Pin up girl
Nice to have
• A crown used on the Q possibly.

```html
<!DOCTYPE html>
<html lang="en">
<head>
<meta charset="utf-8">
<title>Tidy Nook Cleaners – Business Card</title>
<link rel="stylesheet" href="https://fonts.googleapis.com/css2?family=Open+Sans:wght@300;400&display=swap">
<style>
  :root {
    --teal: #58d6cb;
    --teal-deep: #45c3b8;
    --ink: #111111;
    --paper: #f4f4f4;
    --paper-shade: #e6e6e6;
    --stage: #e9e6e1;
    --white: #ffffff;
    --text-grey: #333333;
  }
  * { margin: 0; padding: 0; box-sizing: border-box; }
  html, body { width: 1200px; height: 1023px; overflow: hidden; }
  body {
    background: var(--stage);
    font-family: "Open Sans", sans-serif;
    position: relative;
  }
  .card {
    position: absolute;
    width: 580px;
    height: 330px;
    border-radius: 22px;
    overflow: hidden;
    box-shadow: 0 10px 24px rgba(0,0,0,0.18);
  }

  /* Front */
  .card-front {
    left: 60px; top: 110px;
    background: radial-gradient(ellipse at 60% 35%, #64e0d6 0%, var(--teal) 55%, var(--teal-deep) 100%);
  }
  .front-figure {
    position: absolute;
    left: 36px; top: 78px;
    width: 124px; height: 174px;
  }
  .front-name {
    position: absolute;
    left: 174px; top: 138px;
    width: 372px;
    font-size: 38px;
    font-weight: 400;
    color: var(--white);
    letter-spacing: -0.5px;
    line-height: 1;
    white-space: nowrap;
  }
  .front-web {
    position: absolute;
    right: 44px; bottom: 42px;
    font-size: 18px;
    font-weight: 300;
    color: var(--white);
    letter-spacing: 0.5px;
  }

  /* Back */
  .card-back {
    left: 560px; top: 580px;
    background: radial-gradient(ellipse at 50% 45%, var(--white) 0%, var(--paper) 60%, var(--paper-shade) 100%);
  }
  .name-band {
    position: absolute;
    left: 0; top: 0;
    width: 330px; height: 66px;
    background: var(--teal);
    border-radius: 0 33px 33px 0;
    padding: 8px 0 0 34px;
  }
  .person-name {
    font-size: 24px; font-weight: 300;
    color: var(--white); line-height: 1.1;
  }
  .person-title {
    font-size: 14px; color: var(--ink); line-height: 1.2;
  }
  .contact-list {
    position: absolute;
    left: 34px; top: 86px;
    list-style: none;
    font-size: 14px;
    color: var(--text-grey);
    line-height: 1.55;
  }
  .contact-list li { display: flex; align-items: center; gap: 6px; }
  .contact-list svg { width: 12px; height: 12px; }
  .back-figure {
    position: absolute;
    right: 46px; bottom: 96px;
    width: 110px; height: 70px;
  }
  .back-name {
    position: absolute;
    right: 34px; bottom: 54px;
    font-size: 30px; font-weight: 400;
    color: var(--teal-deep);
    letter-spacing: -0.5px;
    white-space: nowrap;
  }
  .service-line {
    position: absolute;
    left: 34px; bottom: 22px;
    font-size: 13.5px;
    color: var(--text-grey);
    display: flex; align-items: center; gap: 6px;
  }
  .service-line .dot {
    width: 7px; height: 7px; border-radius: 50%;
    background: var(--teal-deep);
  }
</style>
</head>
<body>

<section class="card card-front">
  <svg class="front-figure" viewBox="0 0 124 174" role="img" aria-label="Pin-up maid silhouette holding a feather duster">
    <rect width="124" height="174" rx="14" fill="#111111"/>
  </svg>
  <div class="front-name">Tidy Nook Cleaners</div>
  <div class="front-web">www.tidynook.com</div>
</section>

<section class="card card-back">
  <div class="name-band">
    <div class="person-name">Mira Delgado</div>
    <div class="person-title">Title</div>
  </div>

  <ul class="contact-list">
    <li>
      <svg viewBox="0 0 12 12"><path d="M6 0.5a4 4 0 0 1 4 4c0 3-4 7-4 7s-4-4-4-7a4 4 0 0 1 4-4z" fill="#333"/><circle cx="6" cy="4.5" r="1.4" fill="#fff"/></svg>
      Your Address
    </li>
    <li>
      <svg viewBox="0 0 12 12"><circle cx="6" cy="6" r="5.2" fill="none" stroke="#333" stroke-width="1"/><path d="M4 3.5l1 1-.6.8c.4.9 1.1 1.6 2 2l.8-.6 1 1-.8.9c-2-.4-3.9-2.3-4.3-4.3z" fill="#333"/></svg>
      555-014-2290
    </li>
    <li>
      <svg viewBox="0 0 12 12"><rect x="0.7" y="2.5" width="10.6" height="7" fill="none" stroke="#333" stroke-width="1"/><path d="M0.7 2.5L6 6.5l5.3-4" fill="none" stroke="#333" stroke-width="1"/></svg>
      hello@tidynook.com
    </li>
  </ul>

  <svg class="back-figure" viewBox="0 0 110 70" role="img" aria-label="Small pin-up maid silhouette with duster">
    <rect width="110" height="70" rx="10" fill="#111111"/>
  </svg>
  <div class="back-name">Tidy Nook Cleaners</div>

  <div class="service-line">
    <span>Service 1</span><span class="dot"></span>
    <span>Service 2</span><span class="dot"></span>
    <span>Service 3</span><span class="dot"></span>
    <span>Service 4</span><span class="dot"></span>
    <span>Service 5</span><span class="dot"></span>
    <span>Service 6</span>
  </div>
</section>

</body>
</html>
```